Copperleaf Motorized Shade Business Card

Hello, we've had our logo made. Now we are looking for a clean and cool looking business card. One side can just be the logo with any design elements that might look good with it. The other side will be Name, Phone Number and Email. There will not be an address on the card.

```html
<!DOCTYPE html>
<html lang="en">
<head>
<meta charset="utf-8">
<title>Copperleaf Motorized Shade – Business Card</title>
<link rel="stylesheet" href="https://fonts.googleapis.com/css2?family=Roboto:wght@400;500&family=Montserrat:wght@700&display=swap">
<style>
  :root {
    --backdrop: #e4e4e2;
    --card-white: #ffffff;
    --card-dark: #2e2e2e;
    --navy: #0f3a7a;
    --sky: #1ea0e6;
    --ink: #1f3560;
    --edge: #22a7ec;
  }
  * { box-sizing: border-box; margin: 0; padding: 0; }
  html, body { width: 1200px; height: 801px; overflow: hidden; }
  body {
    background: var(--backdrop);
    font-family: "Roboto", Arial, sans-serif;
    position: relative;
  }
  .card {
    position: absolute;
    top: 252px;
    width: 520px;
    height: 297px;
    border-bottom: 4px solid var(--edge);
    box-shadow: 0 6px 18px rgba(0,0,0,0.18);
    overflow: hidden;
  }
  .card--front { left: 50px; background: var(--card-white); }
  .card--back { left: 630px; background: var(--card-dark); }

  .brand-name {
    position: absolute;
    font-family: "Montserrat", Arial, sans-serif;
    font-weight: 700;
    color: var(--navy);
    text-align: right;
    line-height: 1;
    white-space: nowrap;
  }
  .brand-main { display: block; }
  .brand-sub { display: block; }

  /* front */
  .card--front .brand-name { right: 40px; top: 46px; }
  .card--front .brand-main { font-size: 34px; letter-spacing: 0.5px; }
  .card--front .brand-sub { font-size: 10px; letter-spacing: 3.6px; margin-top: 6px; }

  .person {
    position: absolute;
    left: 40px;
    top: 128px;
  }
  .person-name { font-size: 22px; font-weight: 500; color: var(--sky); line-height: 1.2; }
  .person-role { font-size: 15px; color: var(--ink); margin-top: 2px; line-height: 1.2; }
  .divider {
    position: absolute;
    left: 40px;
    right: 40px;
    top: 176px;
    height: 1.5px;
    background: var(--navy);
  }
  .contact-list {
    position: absolute;
    left: 40px;
    top: 192px;
    list-style: none;
    font-size: 14px;
    color: var(--ink);
  }
  .contact-list li { display: flex; align-items: center; gap: 9px; height: 24px; white-space: nowrap; }
  .contact-list svg { width: 12px; height: 12px; fill: var(--sky); flex: none; }

  /* back */
  .card--back .brand-name { right: 30px; top: 34px; }
  .card--back .brand-main { font-size: 40px; letter-spacing: 0.5px; }
  .card--back .brand-sub { font-size: 12px; letter-spacing: 4.5px; margin-top: 8px; }
  .shade-art {
    position: absolute;
    left: 0;
    bottom: 0;
    width: 300px;
    height: 170px;
    background: linear-gradient(135deg, #1c1c1c 0%, #3a3a3a 55%, #8a8a8a 85%, #b5b5b5 100%);
  }
</style>
</head>
<body>
  <section class="card card--front" aria-label="Business card front">
    <div class="brand-name">
      <span class="brand-main">COPPERLEAF</span>
      <span class="brand-sub">MOTORIZED SHADES</span>
    </div>
    <div class="person">
      <p class="person-name">Daniel Reyes</p>
      <p class="person-role">Manager</p>
    </div>
    <div class="divider"></div>
    <ul class="contact-list">
      <li>
        <svg viewBox="0 0 24 24" aria-hidden="true"><path d="M6.6 10.8a15.1 15.1 0 0 0 6.6 6.6l2.2-2.2a1 1 0 0 1 1-.25 11.4 11.4 0 0 0 3.6.57 1 1 0 0 1 1 1V20a1 1 0 0 1-1 1A17 17 0 0 1 3 4a1 1 0 0 1 1-1h3.5a1 1 0 0 1 1 1c0 1.25.2 2.45.57 3.6a1 1 0 0 1-.25 1z"/></svg>
        <span>555-014-2100</span>
      </li>
      <li>
        <svg viewBox="0 0 24 24" aria-hidden="true"><path d="M2 5h20v14H2zm2 2v.5l8 5 8-5V7zm0 2.8V17h16V9.8l-8 5z"/></svg>
        <span>daniel@copperleafshades.com</span>
      </li>
      <li>
        <svg viewBox="0 0 24 24" aria-hidden="true"><path d="M12 2a10 10 0 1 0 0 20 10 10 0 0 0 0-20zm6.9 6h-3a15.6 15.6 0 0 0-1.3-3.6A8 8 0 0 1 18.9 8zM12 4a13.9 13.9 0 0 1 1.9 4h-3.8A13.9 13.9 0 0 1 12 4zM4.3 14a8 8 0 0 1 0-4h3.4a16 16 0 0 0 0 4zm.8 2h3a15.6 15.6 0 0 0 1.3 3.6A8 8 0 0 1 5.1 16zm3-8h-3a8 8 0 0 1 4.3-3.6A15.6 15.6 0 0 0 8.1 8zM12 20a13.9 13.9 0 0 1-1.9-4h3.8A13.9 13.9 0 0 1 12 20zm2.3-6H9.7a14.5 14.5 0 0 1 0-4h4.6a14.5 14.5 0 0 1 0 4zm.3 5.6a15.6 15.6 0 0 0 1.3-3.6h3a8 8 0 0 1-4.3 3.6zM16.3 14a16 16 0 0 0 0-4h3.4a8 8 0 0 1 0 4z"/></svg>
        <span>www.copperleafshades.com</span>
      </li>
    </ul>
  </section>

  <section class="card card--back" aria-label="Business card back">
    <div class="brand-name">
      <span class="brand-main">COPPERLEAF</span>
      <span class="brand-sub">MOTORIZED SHADES</span>
    </div>
    <div class="shade-art" role="img" aria-label="Dark illustration of window shade slats beside a setting sun"></div>
  </section>
</body>
</html>
```